Pixlog Business Card For Comedian

Hi,

I'd like a 2-sided business card that kind mimics an Pixlog page. I've attached screenshots with the copy and language that should be written on there.

I'd like it to be way more stylized and a bit more creative than what I did on Powerpoint. I just did a mockup so that you can have an idea. I'd like it to be designed and you to take a bit of creative imagery so that it doesn't look so static and monochromatic.

PLEASE BE CREATIVE WITH THESE DESIGNS. I DON'T WANT IT TO LOOK EXACTLY LIKE THE ATTACHED IMAGE OR EXACTLY LIKE AN PIXLOG PAGE. I want to use it as inspiration to create something that looks more sleek, and creative. I don't want the colors to just be boring gray, and blue. Have fun and spice it up a bit!

Check out my website LornaFabish.com to see the colors and fonts I use for my branding.

For the main photo: Here's a link with the hi-res photo: !https://www.filecrate-example.com/s/q8ktw3rmpadvhje/Lorna-Fabish-C71B2204.jpg?dl=0

For the thumbnail icon photo, you can use this: https://www.filecrate-example.com/s/xo5nvte2gwhrbsk/Lorna%20Fabish%20Tin%20Vale%20Headshot.jpg?dl=0

Use the Standard Business Card Template from Quillprint.com:
https://help.quillprint-example.com/hc/en-us/article_attachments/309827164/Standard_Size__US__Business_Cards_Portrait.jpg

Please let me know if you have any questions.
Updates

Industry/Entity Type

Business

Contact Information for Business Card

All of the text and copy has been provided on the attached jpg.

Colors
33a6d7
0255a3
aaaaaa
dbdbdb
1b1b1b

Requirements
Should not have
• A Hyperlink for the Email Addresses

```html
<!DOCTYPE html>
<html lang="en">
<head>
<meta charset="utf-8">
<title>Lorna Fabish – Business Card</title>
<link rel="stylesheet" href="https://fonts.googleapis.com/css2?family=Nunito+Sans:ital,wght@0,400;0,600;0,700;0,800;1,400&display=swap">
<style>
  :root {
    --sky: #33a6d7;
    --navy: #0255a3;
    --grey: #aaaaaa;
    --mist: #dbdbdb;
    --ink: #1b1b1b;
    --paper: #ffffff;
    --stage: #eef1f4;
    --skyline: #d6ecf7;
    --photo-hair: #2a1d18;
    --photo-skin: #6b3f2c;
    --photo-top: #c9564a;
  }
  * { box-sizing: border-box; margin: 0; padding: 0; }
  html, body { width: 1200px; height: 1000px; overflow: hidden; }
  body {
    background: var(--stage);
    font-family: "Nunito Sans", Arial, sans-serif;
    color: var(--ink);
    position: relative;
  }
  .card {
    position: absolute;
    top: 145px;
    width: 400px;
    height: 700px;
    background: var(--paper);
    box-shadow: 0 10px 30px rgba(0,0,0,.18);
    overflow: hidden;
  }
  .card--profile { left: 170px; }
  .card--feed { left: 630px; }

  .skyline {
    position: absolute;
    left: 0; right: 0; bottom: 0;
    height: 120px;
    background: linear-gradient(to top, var(--skyline), rgba(214,236,247,0));
  }

  /* Profile side */
  .profile__header {
    height: 64px;
    background: var(--sky);
    color: var(--paper);
    font-weight: 700;
    font-size: 24px;
    letter-spacing: 3px;
    text-align: center;
    line-height: 64px;
  }
  .profile__top {
    position: relative;
    padding: 24px 24px 0 24px;
    height: 260px;
  }
  .avatar {
    border-radius: 50%;
    background: radial-gradient(circle at 50% 40%, var(--photo-skin), var(--photo-hair) 70%);
  }
  .profile__avatar {
    position: absolute;
    left: 24px; top: 24px;
    width: 104px; height: 104px;
  }
  .contact-row {
    display: flex;
    justify-content: flex-end;
    align-items: center;
    gap: 14px;
    text-align: right;
  }
  .contact-row svg { flex: none; width: 34px; height: 34px; stroke: var(--grey); fill: none; stroke-width: 2; }
  .profile__name { font-weight: 800; font-size: 22px; margin-top: 4px; }
  .profile__site { font-size: 17px; margin-top: 16px; }
  .profile__booking-label { color: var(--sky); font-size: 17px; font-weight: 600; text-align: right; padding-right: 48px; margin-top: 12px; }
  .profile__emails { font-size: 16px; line-height: 1.35; }

  .section-tab {
    display: inline-block;
    background: var(--grey);
    color: var(--paper);
    font-weight: 700;
    font-size: 21px;
    letter-spacing: 3px;
    padding: 2px 18px 2px 44px;
    margin-top: 22px;
  }
  .about {
    padding: 8px 20px 0;
    font-size: 15px;
    line-height: 1.4;
  }
  .about__seen { font-style: italic; margin-top: 18px; }
  .social { list-style: none; padding: 10px 24px; font-size: 16px; line-height: 1.55; }
  .social li { display: flex; align-items: center; gap: 8px; }
  .social__dot { width: 10px; height: 10px; border-radius: 50%; background: var(--sky); }
  .social__net { color: var(--sky); font-weight: 600; }

  /* Feed side */
  .feed__strip { height: 12px; background: var(--sky); }
  .feed__head {
    display: flex;
    align-items: center;
    gap: 12px;
    padding: 12px 16px;
    height: 82px;
  }
  .feed__avatar { width: 56px; height: 56px; }
  .feed__handle { font-weight: 800; font-size: 22px; line-height: 1.1; }
  .feed__place { color: var(--sky); font-weight: 600; font-size: 19px; }
  .feed__photo {
    position: relative;
    height: 380px;
    background: radial-gradient(ellipse 40% 45% at 50% 40%, var(--photo-skin), var(--photo-hair) 75%),
                var(--photo-hair);
  }
  .feed__photo::after {
    content: "";
    position: absolute; left: 0; right: 0; bottom: 0; height: 90px;
    background: linear-gradient(to top, var(--photo-top), rgba(201,86,74,0));
  }
  .feed__actions {
    position: absolute; left: 14px; bottom: 14px; z-index: 1;
    display: flex; gap: 12px;
  }
  .feed__actions svg { width: 30px; height: 30px; stroke: var(--paper); fill: none; stroke-width: 2; opacity: .85; }
  .feed__caption {
    position: relative; z-index: 1;
    padding: 14px 22px;
    font-size: 16px;
    line-height: 1.3;
    text-transform: uppercase;
    word-break: break-word;
  }
  .feed__caption .lead { text-transform: none; }
</style>
</head>
<body>

<section class="card card--profile">
  <header class="profile__header">PROFILE</header>
  <div class="profile__top">
    <div class="avatar profile__avatar" role="img" aria-label="Headshot of Lorna Fabish"></div>
    <div class="contact-row">
      <span class="profile__name">Lorna Fabish</span>
      <svg viewBox="0 0 34 34"><circle cx="17" cy="12" r="7"/><path d="M4 31c0-8 6-11 13-11s13 3 13 11z"/></svg>
    </div>
    <div class="contact-row profile__site">
      <span>LornaFabish.com</span>
      <svg viewBox="0 0 34 34"><circle cx="17" cy="17" r="14"/><ellipse cx="17" cy="17" rx="6" ry="14"/><path d="M3 17h28M5 10h24M5 24h24"/></svg>
    </div>
    <p class="profile__booking-label">For Booking:</p>
    <div class="contact-row">
      <span class="profile__emails">Dana@BrightlineTalent.com<br>Mara.Quinlan@tgny.com</span>
      <svg viewBox="0 0 34 34"><rect x="3" y="8" width="28" height="19"/><path d="M3 8l14 11 14-11"/></svg>
    </div>
  </div>

  <h2 class="section-tab">ABOUT</h2>
  <div class="about">
    <p>Stand Up Comedian | Host | Writer | Actor | Dance<br>
    I do not sing unless I'm in the shower<br>
    I accept tips. <em>Not on jokes, but on Cashly.</em></p>
    <p class="about__seen">As seen on HVN, Laugh Central, QTV,<br>Real TV, Vantage and BNX.</p>
  </div>

  <h2 class="section-tab">MORE INFO</h2>
  <ul class="social">
    <li><span class="social__dot"></span><span class="social__net">Friendwall</span> /LornaFabish</li>
    <li><span class="social__dot"></span><span class="social__net">Chirp</span> /Tinfab</li>
    <li><span class="social__dot"></span><span class="social__net">Pixlog</span> /Tinfab</li>
  </ul>
  <div class="skyline" role="img" aria-label="Faint city skyline"></div>
</section>

<section class="card card--feed">
  <div class="feed__strip"></div>
  <div class="feed__head">
    <div class="avatar feed__avatar" role="img" aria-label="Small headshot of Lorna Fabish"></div>
    <div>
      <p class="feed__handle">tinfab</p>
      <p class="feed__place">Brooklyn, New York</p>
    </div>
  </div>
  <div class="feed__photo" role="img" aria-label="Portrait photo of Lorna Fabish">
    <div class="feed__actions">
      <svg viewBox="0 0 30 30"><path d="M15 26S3 18 3 10a6 6 0 0 1 12-2 6 6 0 0 1 12 2c0 8-12 16-12 16z"/></svg>
      <svg viewBox="0 0 30 30"><circle cx="12" cy="12" r="8"/><path d="M18 18l9 9"/></svg>
      <svg viewBox="0 0 30 30"><circle cx="20" cy="9" r="6"/><path d="M16 13L5 26M8 20l3 3"/></svg>
    </div>
  </div>
  <p class="feed__caption"><span class="lead">Your favorite comic's favorite comic.</span> #ISAIDIT #SOITSTRUE #FINDME #FOLLOWME #NOTTOMYHOUSE #POSTABOUTME #USINGTHESEHASTAGS #LORNAFABISH #TINFAB #IMSUCHABROOKLYNGIRL #MAKENYUNSAFEAGAIN #BROOKLYNSTANDUPCOMEDY</p>
  <div class="skyline" role="img" aria-label="Faint city skyline"></div>
</section>

</body>
</html>
```